Brightwall Residences Estepona listings flyer

Brightwall Residences Estepona are a specialist estate agency focussed solely on selling modern and contemporary homes.

We need an A4 folded flyer to be designed so that Brightwall Residences Estepona can leaflet drop all of the modern homes for sale in our area to generate new instructions / listings. We need to engage with owners of those types of homes by posting this marketing material through their letter boxes in the hope that they see our funky and modern design and decide to call us about our services to sell their home, if for sale.

We would like to see sharp lines and a modern design (see our logo for style and colour scheme), with lots of white spaces and using photos which can blend in to the background to provide a powerful and impacting image to set us aside from any other direct mail leaflets which may be in their post box. It needs to show

* Quality
* Style
* Modern and forward thinking in design and outlook
* Professionalism

Front page
Top:
Logo of Brightwall Residences Estepona.
Guiding your sleek property to its buyer. Nothing else!

4 property photos in a grid position

Bottom banner
If you are thinking of selling, read on…

INSIDE LEFT & RIGHT (DOUBLE PAGE POSSIBLY BLANK WHITE BACKGROUND)
Title: Use Brightwall Residences Estepona – the specialist modern homes agency to sell your home

We bring an exciting and dynamic mix of modern marketing with good old fashioned service to guarantee only the most qualified clients will be viewing your home (use online marketing image)

Marketing packages include stylish online brochures, professional photography, stunning drone video footage, informative video walk thru’s and unique floor plans (use drone and floor plan images)

Targeted social media campaigns focusing on international clientele actively looking to buy property in southern Spain (use social media image)

Bespoke, powerful advertising packages enable worldwide exposure for both online and traditional channels to market. We can be as discreet or as visible as you want us to be to sell your home

During our 20 years on the Costa del Sol, we have built up an enviable network of collaborating agents meaning you only have to instruct one expert real estate agent, Brightwall Residences Estepona, to gain maximum exposure for your home

BACK PAGE

If you want service that matches the value of your home, contact us today for a private, personalised consultation. Brightwall Residences Estepona. Nothing else.

Suite 14
Torrevaca Office Park
Calle Los Almendros
Torrevaca, Marbella

Tel: +34 952 418 360
Mobil y Whatsapp: +34 687 530 271
Email: info@brightwallresidencesestepona.example
www.brightwallresidencesestepona.example

Target Market(s)

Wealthy property owners of contemporary and modern homes who are looking to sell their home

Industry/Entity Type

Real Estate Agent

Font styles to use
Serif
Sans Serif

Colors
606060
e7e7e7
f5f5f5

Requirements
Must have
• Classy, professional, modern design with the ability to stand out from other leaflet drops / direct mail in letter box
Nice to have
• straight lines to border photos
• Maybe extend the lines further than they should so it has the look of an architects plan
• Blend in images to white background in the middle open double page
Should not have
• Lots of different colours

```html
<!DOCTYPE html>
<html lang="en">
<head>
<meta charset="utf-8">
<title>Brightwall Residences Estepona – Front Panel</title>
<link rel="stylesheet" href="https://fonts.googleapis.com/css2?family=Open+Sans:wght@400;600;700&display=swap">
<style>
  :root {
    --page-bg: #d9d9db;
    --paper: #ffffff;
    --paper-shade: #f5f5f5;
    --paper-soft: #e7e7e7;
    --ink: #606060;
    --ink-dark: #4a4a4a;
    --frame-line: #c9c9c9;
  }
  * { margin: 0; padding: 0; box-sizing: border-box; }
  html, body {
    width: 1200px;
    height: 900px;
    overflow: hidden;
    background: var(--page-bg);
    font-family: "Open Sans", Arial, sans-serif;
  }
  .front-panel {
    position: absolute;
    left: 402px;
    top: 30px;
    width: 396px;
    height: 840px;
    background: linear-gradient(160deg, var(--paper) 0%, var(--paper-shade) 55%, var(--paper-soft) 100%);
    box-shadow: 0 2px 10px rgba(0,0,0,0.12);
    overflow: hidden;
  }
  .brand {
    position: absolute;
    top: 52px;
    right: 44px;
    display: flex;
    align-items: center;
    gap: 8px;
    color: var(--ink-dark);
    font-size: 11px;
    font-weight: 700;
    letter-spacing: 0.06em;
    text-transform: uppercase;
  }
  .brand-square {
    width: 14px;
    height: 14px;
    background: var(--ink-dark);
  }
  .photo-grid {
    position: absolute;
    left: 0;
    top: 0;
    width: 396px;
    height: 840px;
  }
  .selling-prompt {
    position: absolute;
    right: 34px;
    bottom: 92px;
    text-align: right;
    color: var(--ink);
  }
  .selling-prompt .lead {
    font-size: 13px;
    font-weight: 400;
    letter-spacing: 0.01em;
  }
  .selling-prompt .read-on {
    font-size: 24px;
    font-weight: 700;
    color: var(--ink-dark);
    line-height: 1.15;
  }
</style>
</head>
<body>
  <section class="front-panel">
    <div class="brand">
      <span class="brand-square"></span>
      <span class="brand-name">Brightwall Residences Estepona</span>
    </div>

    <svg class="photo-grid" viewBox="0 0 396 840" xmlns="http://www.w3.org/2000/svg">
      <defs>
        <linearGradient id="tone-terrace" x1="0" y1="0" x2="0" y2="1">
          <stop offset="0" stop-color="#8fa9c4"/>
          <stop offset="0.35" stop-color="#b8734a"/>
          <stop offset="1" stop-color="#5a4a30"/>
        </linearGradient>
        <linearGradient id="tone-night" x1="0" y1="0" x2="1" y2="1">
          <stop offset="0" stop-color="#1c2e42"/>
          <stop offset="0.55" stop-color="#3e4f5c"/>
          <stop offset="1" stop-color="#0f1d2c"/>
        </linearGradient>
        <linearGradient id="tone-facade" x1="0" y1="0" x2="0" y2="1">
          <stop offset="0" stop-color="#4d7fd6"/>
          <stop offset="0.45" stop-color="#e9edf0"/>
          <stop offset="1" stop-color="#2e4a52"/>
        </linearGradient>
        <linearGradient id="tone-pool" x1="0" y1="0" x2="0" y2="1">
          <stop offset="0" stop-color="#2a78c8"/>
          <stop offset="0.45" stop-color="#f0f2f2"/>
          <stop offset="1" stop-color="#3fb3d9"/>
        </linearGradient>
      </defs>

      <g class="frame-lines" fill="none" stroke="var(--frame-line)" stroke-width="1">
        <polygon points="190,230 140,143 40,143 -10,230 40,317 140,317"/>
        <polygon points="340,317 290,230 190,230 140,317 190,404 290,404"/>
        <polygon points="190,404 140,317 40,317 -10,404 40,491 140,491"/>
        <polygon points="340,491 290,404 190,404 140,491 190,578 290,578"/>
      </g>

      <polygon role="img" aria-label="Photo of a modern home with terracotta walls and a glazed balcony"
               fill="url(#tone-terrace)" points="186,230 138,146.9 42,146.9 -6,230 42,313.1 138,313.1"/>
      <polygon role="img" aria-label="Photo of a contemporary villa lit up at night"
               fill="url(#tone-night)" points="336,317 288,233.9 192,233.9 144,317 192,400.1 288,400.1"/>
      <polygon role="img" aria-label="Photo of a white modern facade with glass and palms under blue sky"
               fill="url(#tone-facade)" points="186,404 138,320.9 42,320.9 -6,404 42,487.1 138,487.1"/>
      <polygon role="img" aria-label="Photo of a white villa beside a turquoise swimming pool"
               fill="url(#tone-pool)" points="336,491 288,407.9 192,407.9 144,491 192,574.1 288,574.1"/>
    </svg>

    <div class="selling-prompt">
      <p class="lead">If you are thinking of selling,</p>
      <p class="read-on">Read on...</p>
    </div>
  </section>
</body>
</html>
```